R & T Summit Construction Business Card ideas

We want a business card to represents our company in a way that looks professional but is also a business card that is unique!

Industry/Entity Type

Construction Company

Contact Information for Business Card

open to all design ideas, just want to be able to see different options to choose from in either color or grayscale.

Requirements
Must have
• Our names and phone numbers
• Mark Hollis 386-555-0142
• Derek Walsh 386-555-0187
• Business logo

```html
<!DOCTYPE html>
<html lang="en">
<head>
<meta charset="utf-8">
<title>R &amp; T Summit Construction – Business Card</title>
<link href="https://fonts.googleapis.com/css2?family=Open+Sans:wght@400;600;700&display=swap" rel="stylesheet">
<style>
  :root {
    --backdrop: #e4e2df;
    --card-white: #ffffff;
    --card-black: #050505;
    --ink: #111111;
    --ink-soft: #222222;
  }
  * { margin: 0; padding: 0; box-sizing: border-box; }
  html, body {
    width: 1200px; height: 1000px; overflow: hidden;
    background: var(--backdrop);
    font-family: "Open Sans", Arial, sans-serif;
  }
  .canvas { position: relative; width: 1200px; height: 1000px; }
  .card {
    position: absolute; left: 267px; width: 665px; height: 395px;
    border-radius: 24px; overflow: hidden;
    box-shadow: 0 6px 16px rgba(0,0,0,0.18);
  }
  .card--front { top: 75px; background: var(--card-white); color: var(--ink); }
  .card--back { top: 535px; background: var(--card-black); }

  .contact { position: absolute; left: 32px; top: 58px; }
  .contact__name { font-weight: 600; font-size: 19px; letter-spacing: 0.2px; line-height: 24px; }
  .contact__line {
    display: flex; align-items: center; gap: 6px;
    font-size: 16px; line-height: 22px; color: var(--ink-soft);
  }
  .contact__line svg { width: 12px; height: 12px; flex: none; }
  .contact__person + .contact__person { margin-top: 10px; }
  .contact__address { margin-top: 14px; font-size: 15.5px; line-height: 25px; color: var(--ink-soft); }
  .contact__web { margin-top: 14px; }
  .contact__web .contact__line { font-size: 16px; line-height: 25px; }

  .brand-name {
    position: absolute; font-weight: 600; text-transform: uppercase;
    letter-spacing: 1px; line-height: 1.15; text-align: center;
  }
  .card--front .brand-name { left: 335px; top: 170px; width: 300px; font-size: 25px; color: var(--ink); }
  .card--back .brand-name { left: 130px; top: 150px; width: 405px; font-size: 33px; color: var(--card-white); }

  .wave { position: absolute; left: 0; bottom: 0; width: 665px; height: 90px; }
</style>
</head>
<body>
<main class="canvas">
  <section class="card card--front" aria-label="Business card front">
    <div class="contact">
      <div class="contact__person">
        <p class="contact__name">MARK HOLLIS</p>
        <p class="contact__line">
          <svg viewBox="0 0 24 24" aria-hidden="true"><path fill="#111" d="M6.6 10.8c1.4 2.8 3.8 5.1 6.6 6.6l2.2-2.2c.3-.3.7-.4 1-.2 1.1.4 2.3.6 3.6.6.6 0 1 .4 1 1V20c0 .6-.4 1-1 1C10.6 21 3 13.4 3 4c0-.6.4-1 1-1h3.5c.6 0 1 .4 1 1 0 1.3.2 2.5.6 3.6.1.3 0 .7-.2 1l-2.3 2.2z"/></svg>
          386-555-0142
        </p>
      </div>
      <div class="contact__person">
        <p class="contact__name">DEREK WALSH</p>
        <p class="contact__line">
          <svg viewBox="0 0 24 24" aria-hidden="true"><path fill="#111" d="M6.6 10.8c1.4 2.8 3.8 5.1 6.6 6.6l2.2-2.2c.3-.3.7-.4 1-.2 1.1.4 2.3.6 3.6.6.6 0 1 .4 1 1V20c0 .6-.4 1-1 1C10.6 21 3 13.4 3 4c0-.6.4-1 1-1h3.5c.6 0 1 .4 1 1 0 1.3.2 2.5.6 3.6.1.3 0 .7-.2 1l-2.3 2.2z"/></svg>
          386-555-0187
        </p>
      </div>
      <p class="contact__address">2415 Harbor View Rd 8 St,<br>Linfield, MD 21099</p>
      <div class="contact__web">
        <p class="contact__line">
          <svg viewBox="0 0 24 24" aria-hidden="true"><path fill="#111" d="M2 5h20v14H2z"/><path fill="none" stroke="#fff" stroke-width="2" d="M2 6l10 7 10-7"/></svg>
          info@rtsummitconstruction.com
        </p>
        <p class="contact__line">
          <svg viewBox="0 0 24 24" aria-hidden="true"><circle cx="12" cy="12" r="9" fill="none" stroke="#111" stroke-width="2.5"/><path fill="none" stroke="#111" stroke-width="2" d="M3 12h18M12 3c3 3 3 15 0 18M12 3c-3 3-3 15 0 18"/></svg>
          www.rtsummitconstruction.com
        </p>
      </div>
    </div>

    <p class="brand-name">R &amp; T Summit<br>Construction</p>

    <svg class="wave" viewBox="0 0 665 90" preserveAspectRatio="none" aria-hidden="true">
      <path fill="#050505" d="M0 82 C40 52 90 30 150 26 C300 16 450 42 560 42 C620 42 650 32 665 24 L665 90 L0 90 Z"/>
      <path fill="none" stroke="#fff" stroke-width="3" d="M5 88 C100 66 250 46 380 51 C500 56 600 52 655 30"/>
    </svg>
  </section>

  <section class="card card--back" aria-label="Business card back">
    <p class="brand-name">R &amp; T Summit<br>Construction</p>
  </section>
</main>
</body>
</html>
```